New business Cards

We need some new cards that stand out. We love our logo and colour scheme but need to incorporate a qubo logo and bfn logo yet still keep our cards uncluttered and clean looking.
Our tag is Bright Ledger. Anywhere, Anytime.
The idea of the cards is to show authority in accounting and Talvo/ cloud software

```html
<!DOCTYPE html>
<html lang="en">
<head>
<meta charset="utf-8">
<title>Halden Business Cards</title>
<link href="https://fonts.googleapis.com/css2?family=Tinos:wght@400&family=Arimo:wght@400&display=swap" rel="stylesheet">
<style>
  :root {
    --bg: #b9b9b9;
    --card: #ffffff;
    --card-shade: #ededed;
    --ink: #2b2b2b;
    --ink-soft: #555555;
    --accent: #6ab42d;
    --partner-ink: #4a4a4a;
    --badge: #c8c8c8;
    --rule: #333333;
  }
  * { margin: 0; padding: 0; box-sizing: border-box; }
  html, body { width: 1200px; height: 871px; overflow: hidden; }
  body {
    background: var(--bg);
    font-family: "Tinos", "Times New Roman", serif;
    color: var(--ink);
    position: relative;
  }
  .card {
    position: absolute;
    width: 600px;
    height: 340px;
    background: linear-gradient(160deg, var(--card) 0%, var(--card) 60%, var(--card-shade) 100%);
    box-shadow: 0 10px 24px rgba(0,0,0,0.28);
  }
  .card--front { left: 80px; top: 80px; }
  .card--back { left: 520px; top: 470px; }

  /* company name */
  .brand__name { font-size: 20px; color: var(--accent); letter-spacing: 3px; }

  /* partner names */
  .partners { display: flex; align-items: center; gap: 16px; }
  .partner__name { font-size: 18px; color: var(--partner-ink); letter-spacing: 1px; }
  .badge { width: 30px; height: 30px; border-radius: 50%; background: var(--badge); }

  /* front */
  .front__marks {
    position: absolute; left: 0; right: 0; top: 132px;
    display: flex; justify-content: center; align-items: center; gap: 22px;
  }
  .front__tagline {
    position: absolute; left: 0; right: 0; top: 190px;
    text-align: center; font-size: 17px; letter-spacing: 4px; color: var(--ink-soft);
  }

  /* back */
  .back__brand { position: absolute; left: 40px; top: 34px; }
  .back__person { position: absolute; left: 40px; top: 96px; }
  .back__name { font-size: 15px; letter-spacing: 0.5px; text-decoration: underline; }
  .back__role { font-family: "Arimo", Arial, sans-serif; font-size: 12px; color: var(--accent); margin-top: 1px; }
  .back__rule { position: absolute; height: 1px; background: var(--rule); }
  .back__rule--top { left: 40px; top: 134px; width: 520px; }
  .back__rule--contact { left: 370px; top: 224px; width: 190px; }
  .back__address { position: absolute; left: 40px; top: 148px; font-size: 13px; line-height: 16px; font-style: normal; }
  .back__tagline { position: absolute; left: 40px; bottom: 60px; font-size: 13px; color: var(--ink-soft); }
  .back__contact {
    position: absolute; right: 40px; top: 232px; text-align: right;
    font-size: 13px; line-height: 16px;
  }
  .back__web { letter-spacing: 3px; }
  .back__web em { font-style: normal; color: var(--accent); }
  .back__partners { position: absolute; right: 40px; bottom: 22px; }
</style>
</head>
<body>

  <section class="card card--front" aria-label="Card front">
    <div class="front__marks">
      <span class="brand__name">HALDEN</span>
      <div class="partners">
        <span class="partner__name">BFN</span>
        <span class="partner__name">Talvo</span>
        <span class="badge" role="img" aria-label="Certified advisor badge"></span>
      </div>
    </div>
    <p class="front__tagline">Bright Ledger. Anywhere, Anytime.</p>
  </section>

  <section class="card card--back" aria-label="Card back">
    <span class="brand__name back__brand">HALDEN</span>
    <div class="back__person">
      <p class="back__name">DANIEL KORVAN</p>
      <p class="back__role">Founder</p>
    </div>
    <div class="back__rule back__rule--top"></div>
    <address class="back__address">
      No 12, Lakeview Road<br>
      West Park<br>
      Chennai 600042<br>
      Tamil Nadu, India
    </address>
    <p class="back__tagline">Bright Ledger. Anywhere, Anytime.</p>
    <div class="back__rule back__rule--contact"></div>
    <div class="back__contact">
      <p>91-900 555 0123</p>
      <p>anil.rao@ledgerpoint.com</p>
      <p class="back__web">www.<em>HALDEN</em>.com</p>
    </div>
    <div class="partners back__partners">
      <span class="partner__name">BFN</span>
      <span class="partner__name">Talvo</span>
      <span class="badge" role="img" aria-label="Certified advisor badge"></span>
    </div>
  </section>

</body>
</html>
```